Marketing Brochures and Sales Sheets

Looking for product brochures for our line of touch screens.

For this design we want to incorporate our new color scheme(attached). We are a tech company that specializes in high performance touch screens. This flyer will be the first of 20 or more.

Target Market(s)

AV companies and businesses looking for touch screen solutions

Industry/Entity Type

Technology Equipment

Requirements
Nice to have
• You can check out our competitors flyers. They are called Varolux

```html
<!DOCTYPE html>
<html lang="en">
<head>
<meta charset="utf-8">
<title>PixelTact – Tilted Touch Screen Tables Brochure</title>
<link rel="stylesheet" href="https://fonts.googleapis.com/css2?family=Montserrat:wght@600;700;800&family=Open+Sans:wght@400;600&display=swap">
<style>
  :root{
    --blue:#2e6fd8;
    --ink:#1c1d21;
    --graphite:#34363b;
    --line:#d7dae0;
    --paper:#ffffff;
    --table:#f3f5f9;
    --backdrop:#ddd7d2;
  }
  *{box-sizing:border-box;margin:0;padding:0}
  html,body{width:720px;height:1200px;overflow:hidden;background:var(--backdrop)}
  body{font-family:"Open Sans",Arial,sans-serif;color:var(--ink);position:relative}
  .spread{position:absolute;left:20px;width:680px;height:470px;display:flex;box-shadow:0 6px 18px rgba(0,0,0,.18)}
  .spread--outer{top:90px}
  .spread--inner{top:640px}
  .page{position:relative;width:340px;height:470px;background:var(--paper);overflow:hidden}
  .page svg.shapes{position:absolute;inset:0}
  .abs{position:absolute}
  .photo{position:absolute}
  .brand{font-family:"Montserrat",Arial,sans-serif;font-weight:800;color:var(--blue);font-size:17px;display:flex;align-items:center;gap:5px}
  .brand .dot{width:9px;height:9px;background:var(--blue)}
  .heading{font-family:"Montserrat",Arial,sans-serif;font-weight:700;color:var(--blue);font-size:11px;text-transform:uppercase;letter-spacing:.5px}
  .body-copy{font-size:6.5px;line-height:1.55;color:var(--graphite)}
  .title{font-family:"Montserrat",Arial,sans-serif;font-weight:800;text-transform:uppercase;text-align:right;line-height:1.05;font-size:19px}
  .title .t1{color:var(--ink);display:block}
  .title .t2{color:var(--blue);display:block}
  .web{font-size:7px;color:var(--graphite);font-weight:600}
  .ticks{list-style:none}
  .ticks li{font-size:6.5px;color:var(--graphite);display:flex;align-items:center;gap:5px;margin-bottom:4px}
  .ticks svg{flex:none}
  .pricing{background:var(--blue);color:#fff;border-radius:3px;padding:7px 10px}
  .pricing h3{font-family:"Montserrat",Arial,sans-serif;font-size:12px;font-weight:800;text-align:center;letter-spacing:1px;margin-bottom:5px}
  .price-row{display:flex;justify-content:space-between;font-size:7px;padding:2px 0;border-top:1px solid rgba(255,255,255,.35)}
  .price-row b{font-weight:600}
  .call-label{font-size:7px;color:var(--graphite);font-weight:600}
  .phone{font-family:"Montserrat",Arial,sans-serif;font-weight:800;color:var(--blue);font-size:15px}
  .contact{display:flex;gap:6px}
  .contact span{width:12px;height:12px;border-radius:50%;background:var(--graphite)}
  .spec-bar{background:var(--blue);color:#fff;font-family:"Montserrat",Arial,sans-serif;font-weight:700;font-size:14px;text-align:center;padding:5px 0;border-left:10px solid var(--ink);border-right:10px solid var(--ink)}
  .specs{width:100%;border-collapse:collapse;font-size:6.5px}
  .specs th{background:var(--ink);color:#fff;font-weight:600;padding:4px 5px;text-align:left}
  .specs td{padding:4px 5px;border-bottom:1px solid var(--line);color:var(--graphite)}
  .specs tr:nth-child(even) td{background:var(--table)}
  .specs td:first-child{font-weight:600;color:var(--ink)}
</style>
</head>
<body>

<section class="spread spread--outer">
  <article class="page back-cover">
    <svg class="shapes" viewBox="0 0 340 470">
      <polygon points="340,0 340,120 270,0" fill="var(--blue)"/>
      <polygon points="340,370 340,470 220,470" fill="var(--blue)"/>
      <polygon points="340,420 340,470 280,470" fill="var(--ink)"/>
    </svg>
    <h2 class="heading abs" style="left:22px;top:26px">Our Company</h2>
    <p class="body-copy abs" style="left:22px;top:44px;width:210px">We build rugged, responsive touch tables for showrooms, lobbies and events, designed to engage visitors and simple to install.</p>
    <div class="photo" role="img" aria-label="Photo of a touch screen table in use" style="left:22px;top:84px;width:200px;height:70px;background:linear-gradient(135deg,#c8ccd3,#6b7079)"></div>
    <ul class="ticks abs" style="left:22px;top:166px;width:220px">
      <li><svg width="8" height="8" viewBox="0 0 8 8"><path d="M1 4l2 2 4-5" stroke="var(--blue)" stroke-width="1.5" fill="none"/></svg>Multi-touch glass with fast response</li>
      <li><svg width="8" height="8" viewBox="0 0 8 8"><path d="M1 4l2 2 4-5" stroke="var(--blue)" stroke-width="1.5" fill="none"/></svg>Adjustable tilt from flat to upright</li>
      <li><svg width="8" height="8" viewBox="0 0 8 8"><path d="M1 4l2 2 4-5" stroke="var(--blue)" stroke-width="1.5" fill="none"/></svg>Steel frame built for public spaces</li>
    </ul>
    <div class="pricing abs" style="left:22px;top:222px;width:200px">
      <h3>PRICING</h3>
      <div class="price-row"><span>Table 43 inch</span><b>$ 3,499</b></div>
      <div class="price-row"><span>Table 55 inch</span><b>$ 4,299</b></div>
      <div class="price-row"><span>Table 65 inch</span><b>$ 5,199</b></div>
    </div>
    <p class="call-label abs" style="left:22px;top:320px">Call us today</p>
    <p class="phone abs" style="left:22px;top:332px">(555) 014-0290</p>
    <div class="contact abs" style="left:22px;top:360px"><span></span><span></span><span></span></div>
  </article>

  <article class="page front-cover">
    <div class="photo" role="img" aria-label="Dark photo of people using a touch table" style="left:0;top:0;width:340px;height:290px;background:linear-gradient(160deg,#55585e,#1b1c1f);clip-path:polygon(190px 0,340px 0,340px 290px,70px 290px)"></div>
    <svg class="shapes" viewBox="0 0 340 470">
      <polygon points="0,110 175,0 230,0 0,235" fill="var(--blue)"/>
      <polygon points="0,330 0,470 175,470" fill="var(--blue)"/>
      <polygon points="0,405 0,470 90,470" fill="var(--ink)"/>
    </svg>
    <div class="brand abs" style="left:20px;top:20px"><span class="dot"></span>PixelTact</div>
    <div class="photo" role="img" aria-label="Product photo of the tilted touch screen table" style="left:110px;top:120px;width:150px;height:140px;background:linear-gradient(180deg,#3a3c41,#6a6e76);border-radius:2px"></div>
    <h1 class="title abs" style="right:18px;top:304px"><span class="t1">Tilted Touch</span><span class="t2">Screen Tables</span></h1>
    <p class="web abs" style="right:18px;top:440px">www.pixeltact.com</p>
  </article>
</section>

<section class="spread spread--inner">
  <article class="page inside-left">
    <svg class="shapes" viewBox="0 0 340 470">
      <polygon points="0,150 120,150 0,330" fill="var(--ink)"/>
      <polygon points="0,380 340,330 340,470 0,470" fill="var(--blue)"/>
    </svg>
    <h2 class="heading abs" style="left:22px;top:24px">About Us</h2>
    <p class="body-copy abs" style="left:22px;top:42px;width:296px">Our team designs high performance touch displays for AV integrators, retailers and venues. Each table pairs precise multi-touch glass with a sturdy tilting frame, so content can be shown flat for groups or angled for one person. We test every unit before it ships and support partners from planning to installation.</p>
    <div class="photo" role="img" aria-label="Product photo of the touch table on its tilted stand" style="left:40px;top:150px;width:150px;height:190px;background:linear-gradient(180deg,#3a3c41,#7a7e86);border-radius:2px"></div>
    <div class="photo" role="img" aria-label="Close-up photo of the touch surface" style="left:150px;top:380px;width:80px;height:70px;background:linear-gradient(135deg,#e6e9ee,#9aa1ab);clip-path:polygon(25% 0,75% 0,100% 50%,75% 100%,25% 100%,0 50%)"></div>
    <div class="photo" role="img" aria-label="Photo of the table frame detail" style="left:240px;top:365px;width:80px;height:70px;background:linear-gradient(135deg,#dfe3e9,#8e959f);clip-path:polygon(25% 0,75% 0,100% 50%,75% 100%,25% 100%,0 50%)"></div>
  </article>

  <article class="page inside-right">
    <svg class="shapes" viewBox="0 0 340 470">
      <polygon points="0,370 150,470 0,470" fill="var(--blue)"/>
      <polygon points="0,420 70,470 0,470" fill="var(--ink)"/>
    </svg>
    <div class="brand abs" style="left:0;right:0;top:22px;justify-content:center"><span class="dot"></span>PixelTact</div>
    <div class="spec-bar abs" style="left:22px;right:22px;top:58px">Specifications</div>
    <table class="specs abs" style="left:22px;top:90px;width:296px">
      <tr><th>Feature</th><th>43 inch</th><th>55 inch</th></tr>
      <tr><td>Resolution</td><td>1920 x 1080</td><td>3840 x 2160</td></tr>
      <tr><td>Touch Points</td><td>20 points</td><td>40 points</td></tr>
      <tr><td>Tilt Range</td><td>0 to 80°</td><td>0 to 80°</td></tr>
      <tr><td>Glass</td><td>Tempered 4 mm</td><td>Tempered 4 mm</td></tr>
      <tr><td>Weight</td><td>62 kg</td><td>78 kg</td></tr>
      <tr><td>Power</td><td>110 to 240 V</td><td>110 to 240 V</td></tr>
    </table>
    <div class="photo" role="img" aria-label="Photo of hands using the touch table" style="left:150px;top:320px;width:170px;height:130px;background:linear-gradient(135deg,#e4e8ee,#7d8590);clip-path:polygon(20% 0,100% 0,100% 100%,20% 100%,0 50%)"></div>
  </article>
</section>

</body>
</html>
```